Veltaro Clear Springs needs a new business card design (we produce and sell pure bottled water)

We need a clean modern design for our new business cards, We have an existing logo which ultimately cannot be changed, however it could be slighty improved and the colours adjusted. We have this existing logo on all of our bottles, vehicles etc.

Our company slogan is "Pure down to the last drop".
Along with our relevant company information
(Address, phone, website email etc) we will only be using names and not putting position titles for flexibilty.

We are looking for a clean, minimalist modern design.

You can view our website (if need of an update also!) to see our business.

Contact Information for Business Card

Staff Name : XXXXXX XXXXXX
Address : 8/41 Dunmore St
Halden Flats QLD 4261
Staff Mobile Number : 04XX XXX XXX
Office Phone Number : 07 3915 2047
Staff Email Address : XXXX@veltaroclearsprings.com.au
Website : www.veltaroclearsprings.com.au

Font styles to use
Sans Serif

Colors
cee9f5
33a6d7
0492cd
0455a3
3276b5
85abd2
cedeed

Requirements
Must have
• The ability to edit and change the staff members details as we will need to edit for each respective staff member (7 in total)

```html
<!DOCTYPE html>
<html lang="en">
<head>
<meta charset="utf-8">
<title>Veltaro Clear Springs – Business Card</title>
<link rel="stylesheet" href="https://fonts.googleapis.com/css2?family=Montserrat:wght@400;700&display=swap">
<style>
  :root {
    --brand-blue: #23acd9;
    --ink: #3a3a3a;
    --paper: #ffffff;
  }
  * { margin: 0; padding: 0; box-sizing: border-box; }
  html, body {
    width: 1200px;
    height: 717px;
    overflow: hidden;
    background: var(--paper);
    font-family: "Montserrat", sans-serif;
  }
  .canvas {
    position: relative;
    width: 1200px;
    height: 717px;
  }
  .card-front {
    position: absolute;
    left: 402px;
    top: 94px;
    width: 396px;
    height: 229px;
    background: var(--brand-blue);
    display: flex;
    align-items: center;
    justify-content: center;
  }
  .wordmark {
    font-weight: 700;
    text-transform: uppercase;
    text-align: center;
    line-height: 1.05;
  }
  .wordmark__square {
    display: block;
    margin: 0 auto 10px;
  }
  .card-front .wordmark { color: var(--paper); }
  .card-front .wordmark__square { width: 26px; height: 26px; background: var(--paper); }
  .card-front .wordmark__line1 { display: block; font-size: 27px; letter-spacing: 0.5px; }
  .card-front .wordmark__line2 { display: block; font-size: 15px; letter-spacing: 0.4px; }

  .card-back {
    position: absolute;
    left: 402px;
    top: 350px;
    width: 396px;
    height: 229px;
    background: var(--paper);
  }
  .card-back .brand {
    position: absolute;
    left: 22px;
    top: 58px;
    width: 142px;
  }
  .card-back .wordmark { color: var(--brand-blue); }
  .card-back .wordmark__square { width: 18px; height: 18px; background: var(--brand-blue); margin-bottom: 7px; }
  .card-back .wordmark__line1 { display: block; font-size: 19px; }
  .card-back .wordmark__line2 { display: block; font-size: 10.5px; letter-spacing: 0.2px; }

  .divider {
    position: absolute;
    left: 186px;
    top: 21px;
    width: 1px;
    height: 192px;
    background: var(--brand-blue);
  }
  .details {
    position: absolute;
    left: 211px;
    top: 57px;
    color: var(--ink);
    font-size: 10.3px;
    line-height: 14.5px;
  }
  .staff-name {
    color: var(--brand-blue);
    font-weight: 700;
    font-size: 12.5px;
    letter-spacing: 0.3px;
    margin-bottom: 6px;
  }
  .details p + p { margin-top: 12px; }
  .details .web { color: var(--brand-blue); }
</style>
</head>
<body>
<main class="canvas">
  <section class="card-front" aria-label="Card front">
    <div class="wordmark">
      <span class="wordmark__square"></span>
      <span class="wordmark__line1">Veltaro</span>
      <span class="wordmark__line2">Clear Springs</span>
    </div>
  </section>

  <section class="card-back" aria-label="Card back">
    <div class="brand">
      <div class="wordmark">
        <span class="wordmark__square"></span>
        <span class="wordmark__line1">Veltaro</span>
        <span class="wordmark__line2">Clear Springs</span>
      </div>
    </div>
    <div class="divider"></div>
    <div class="details">
      <h2 class="staff-name">STAFF NAME</h2>
      <p>M: 04XX XXX XXX<br>Ph: 07 3915 2047</p>
      <p>8/41 Dunmore St<br>Halden Flats QLD 4261</p>
      <p>XXXX@veltaroclearsprings.com.au<br><span class="web">www.veltaroclearsprings.com.au</span></p>
    </div>
  </section>
</main>
</body>
</html>
```